Sales and Lettings Boards

Hello, please see attached our sales and lettings boards for our estate agency. These were "designed" by the sign writers. As you can see they are pretty flat and boring - could you work your magic and make them stand out please? I've also attached the logo files. Many thanks, Glen

Target Market(s)

Consumers - residential sale property sales and lettings

Industry/Entity Type

Real Estate Agent

```html
<!DOCTYPE html>
<html lang="en">
<head>
<meta charset="utf-8">
<title>For Sale Board</title>
<link rel="stylesheet" href="https://fonts.googleapis.com/css2?family=Open+Sans:wdth,wght@75..100,400..800&display=swap">
<style>
  :root {
    --stage: #000000;
    --board: #ffffff;
    --band-grey: #48494c;
    --ink: #48494c;
    --brand-green: #62bb4a;
    --note-ink: #000000;
  }
  * { margin: 0; padding: 0; box-sizing: border-box; }
  html, body {
    width: 1200px; height: 800px; overflow: hidden;
    background: var(--stage);
  }
  .board-frame {
    position: absolute; left: 80px; top: 11px;
    width: 1040px; height: 778px;
  }
  .board {
    position: absolute; left: 0; top: 0;
    width: 958px; height: 717px;
    background: var(--board);
    transform: scale(1.0856);
    transform-origin: 0 0;
    font-family: "Open Sans", sans-serif;
    color: var(--ink);
  }
  .accent-block {
    position: absolute; left: 57px; top: 0;
    width: 82px; height: 185px;
    background: var(--brand-green);
  }
  .headline-band {
    position: absolute; left: 139px; top: 0;
    width: 819px; height: 185px;
    background: var(--band-grey);
  }
  .headline {
    position: absolute; right: 50px; top: -4px;
    font-size: 158px; font-weight: 700; font-stretch: 75%;
    line-height: 1; color: var(--board); letter-spacing: 1px;
    white-space: nowrap;
  }
  .phone {
    position: absolute; right: 50px; top: 196px;
    font-size: 92px; font-weight: 700; line-height: 1;
    letter-spacing: -1px; white-space: nowrap;
  }
  .post-note {
    position: absolute; left: 30px; top: 380px;
    transform: translate(-50%, -50%) rotate(-90deg);
    font-family: Arial, "Helvetica", sans-serif;
    font-size: 16px; color: var(--note-ink); white-space: nowrap;
  }
  .feature {
    position: absolute; font-size: 43px; font-weight: 600;
    line-height: 1; white-space: nowrap; letter-spacing: -0.5px;
  }
  .feature--units   { left: 118px; top: 355px; }
  .feature--size    { right: 58px; top: 352px; }
  .feature--loading { left: 118px; top: 422px; }
  .feature--office  { right: 56px; top: 425px; }
  .feature-dot {
    position: absolute; width: 19px; height: 19px; border-radius: 50%;
    background: var(--brand-green);
  }
  .feature-dot--one { left: 521px; top: 369px; }
  .feature-dot--two { left: 477px; top: 440px; }
  .agency-name {
    position: absolute; left: 118px; top: 572px;
    display: flex; align-items: center; gap: 12px;
  }
  .agency-name__mark {
    width: 22px; height: 22px; border-radius: 50%;
    background: var(--brand-green);
  }
  .agency-name__text {
    font-size: 66px; font-weight: 700; line-height: 1;
    color: var(--ink); letter-spacing: -1px;
  }
  .contact {
    position: absolute; left: 513px; top: 586px;
  }
  .contact__name {
    font-size: 38px; font-weight: 600; line-height: 1;
    letter-spacing: -0.3px; white-space: nowrap;
  }
  .contact__web {
    margin-top: 8px;
    font-size: 29px; font-weight: 700; line-height: 1;
    white-space: nowrap; letter-spacing: -0.3px;
  }
</style>
</head>
<body>
  <div class="board-frame">
    <div class="board">
      <div class="accent-block"></div>
      <div class="headline-band">
        <h1 class="headline">FOR SALE</h1>
      </div>

      <p class="phone">01632 960482</p>

      <p class="post-note">50mm Reserved for timber post</p>

      <p class="feature feature--units">9 Units Available</p>
      <span class="feature-dot feature-dot--one"></span>
      <p class="feature feature--size">1,999-2,000 SF</p>

      <p class="feature feature--loading">Grade Loading</p>
      <span class="feature-dot feature-dot--two"></span>
      <p class="feature feature--office">Mezzanine Office</p>

      <div class="agency-name">
        <span class="agency-name__text">NORVALE</span>
        <span class="agency-name__mark"></span>
      </div>

      <div class="contact">
        <p class="contact__name">CLARA DUNMORE</p>
        <p class="contact__web">www.norvale-estates.co.uk</p>
      </div>
    </div>
  </div>
</body>
</html>
```